Label or packaging Design for Hair Care Line

Dear Designer,
We are Corvella, a brand known for our premium hairstyling tools, and we are excited to expand into hair care. We are currently looking for a talented designer to create the label designs for our entire luxury hair care line.
This project is crucial in establishing our visual identity in the hair care market, and we aim to position ourselves alongside premium brands such as LTP, Dorvane Hair Atelier, and Pelmi.
Project Scope
We need a cohesive label design for our hair care line, which includes:
5 products (e.g., shampoo, conditioner, hair oil, styling cream, and a hair mask).
The designs should include:
Front label: Highlighting the product name, key features, and branding.
Our goal is to achieve a design that communicates premium luxury with a touch of professionalism. Below are the specific guidelines to help you align with our vision:
Style and Inspiration
Think of brands like LTP, Dorvane Hair Atelier, and Pelmi.
Luxury and Minimalism: Clean lines, sophisticated typography, and an elegant color palette.
Subtle femininity: premium finishes like metallic accents (gold, silver, or rose gold).
Brand Personality
Premium: Reflecting high quality and exclusivity.
Modern & Professional: Appealing to a refined, professional audience but also suitable for lifestyle-oriented customers.
Warm & Empowering: A brand that celebrates confidence and individuality.
Color Palette
Neutral tones like black, white, accented with metallics (gold or silver) for a luxurious feel.
Colors that feel timeless and elegant rather than trendy or overly bright.
Typography
Use clean, modern fonts (preferably sans-serif or serif for a refined look).
Clear and legible for all product details while maintaining a high-end aesthetic.
Materials and Finishes
Packaging Shape
The label designs should suit a variety of bottle and jar shapes (e.g., cylindrical, flat, or rounded).
Keep scalability in mind so the identity remains consistent across different products.
Deliverables
To understand the aesthetic we are aiming for, here are some brands to use as inspiration:
LTP: For its minimalistic and modern approach.
Dorvane Hair Atelier: For its combination of luxury and professional appeal.
Pelmi: For its soft femininity and lifestyle branding.
we would like to see your designs applied to a variety of packaging types to get an overall impression of how the brand identity works across different product formats. This includes:
A squeeze bottle (e.g., for styling creams or conditioners).
A glass bottle with a dropper (e.g., for a luxurious hair oil).
A shampoo/conditioner bottle (standard pump or flip-top cap).
A spray bottle (e.g., for leave-in treatments or heat protectors).
By creating designs for these different packaging types, we can better evaluate how cohesive and versatile the brand identity will be across the entire product line.

Updates
As you may have noticed from the designs, they don’t quite align with our briefing. The look needs to be clean and professional, similar to Dorvane, LTP, and the other examples we provided. Please address this, and we’ll check it!

Target Market(s)
europe and us
Font styles to use
Other font styles liked:
- century gothic

Look and feel
Each slider illustrates characteristics of the customer's brand and the style your logo design should communicate.

```html
<!DOCTYPE html>
<html lang="en">
<head>
<meta charset="utf-8">
<title>Corvella — Hair Care Labels</title>
<link href="https://fonts.googleapis.com/css2?family=Montserrat:wght@300;600;700&display=swap" rel="stylesheet">
<style>
  :root {
    --backdrop: #dcdcdc;
    --label: #2a2a2b;
    --label-edge: #1e1e1f;
    --ink: #f4f4f4;
    --shampoo: #d35a9d;
    --conditioner: #56cdd0;
  }
  * { margin: 0; padding: 0; box-sizing: border-box; }
  html, body {
    width: 1200px; height: 1200px; overflow: hidden;
    background: var(--backdrop);
    font-family: "Montserrat", sans-serif;
  }
  .label-set {
    position: absolute; inset: 0;
    display: flex; justify-content: center; align-items: center; gap: 60px;
  }
  .label {
    position: relative;
    width: 480px; height: 780px;
    background: var(--label);
    border-top: 5px solid var(--accent);
    box-shadow: 0 0 0 1px var(--label-edge);
    color: var(--ink);
  }
  .label--shampoo { --accent: var(--shampoo); }
  .label--conditioner { --accent: var(--conditioner); }
  .brand-name {
    position: absolute; top: 120px; left: 0; right: 0;
    text-align: center;
    font-weight: 300; font-size: 86px; letter-spacing: 0.01em;
    color: var(--ink);
  }
  .detail-block {
    position: absolute; top: 330px; left: 50px; right: 30px; bottom: 0;
    border-left: 3px solid var(--accent);
    padding-left: 38px;
  }
  .product-name {
    margin-top: 28px;
    font-weight: 700; font-size: 30px; letter-spacing: 0.32em;
    color: var(--accent);
  }
  .description {
    margin-top: 52px;
    font-weight: 600; font-size: 16px; line-height: 1.85; letter-spacing: 0.3em;
    text-transform: uppercase;
  }
  .tagline {
    margin-top: 62px;
    font-weight: 600; font-size: 17px; letter-spacing: 0.3em;
    color: var(--accent);
  }
  .volume {
    margin-top: 10px;
    font-weight: 600; font-size: 17px; letter-spacing: 0.3em;
  }
</style>
</head>
<body>
  <main class="label-set">
    <section class="label label--shampoo">
      <h1 class="brand-name">corvella</h1>
      <div class="detail-block">
        <h2 class="product-name">SHAMPOO</h2>
        <p class="description">Lorem ipsum dolor sit<br>amet consectetuer<br>adipiscing</p>
        <p class="tagline">AD MINIM VENIAM</p>
        <p class="volume">250 ML</p>
      </div>
    </section>
    <section class="label label--conditioner">
      <h1 class="brand-name">corvella</h1>
      <div class="detail-block">
        <h2 class="product-name">CONDITIONER</h2>
        <p class="description">Lorem ipsum dolor sit<br>amet consectetuer<br>adipiscing</p>
        <p class="tagline">AD MINIM VENIAM</p>
        <p class="volume">250 ML</p>
      </div>
    </section>
  </main>
</body>
</html>
```